PL Dunmore Electric Yard Sign

Looking to have a yard sign designed that we can place at projects we are working on. Most likely will be 18" H x 24" W but flexible that we can increase the size if necessary. It should include our logo, our phone # 555-214-7796, website pldunmoreelectric.example and slogan, built on integrity, driven by excellence. Colors should match our brand.

```html
<!DOCTYPE html>
<html lang="en">
<head>
<meta charset="UTF-8">
<title>PL Dunmore Electric Yard Sign</title>
<link href="https://fonts.googleapis.com/css2?family=Montserrat:wght@600;700;800;900&display=swap" rel="stylesheet">
<style>
  :root {
    --brand-red: #e31e2a;
    --brand-navy: #04356b;
    --sign-white: #ffffff;
    --backdrop: #e8ebe6;
  }
  html, body {
    margin: 0;
    padding: 0;
    width: 1200px;
    height: 1200px;
    overflow: hidden;
    background: var(--backdrop);
    font-family: "Montserrat", sans-serif;
  }
  .yard-sign {
    position: absolute;
    left: 50px;
    top: 187px;
    width: 1100px;
    height: 825px;
    background: var(--sign-white);
    overflow: hidden;
    box-shadow: 0 6px 24px rgba(0,0,0,0.12);
  }
  .sign-bands {
    position: absolute;
    inset: 0;
    width: 100%;
    height: 100%;
  }
  .line {
    position: absolute;
    left: 0;
    width: 100%;
    text-align: center;
    white-space: nowrap;
    margin: 0;
  }
  .brand-name {
    top: 140px;
    font-size: 60px;
    line-height: 72px;
    font-weight: 800;
    letter-spacing: 4px;
    color: var(--brand-red);
    text-transform: uppercase;
  }
  .brand-trade {
    top: 212px;
    font-size: 25px;
    line-height: 32px;
    font-weight: 800;
    letter-spacing: 7px;
    color: var(--brand-navy);
  }
  .brand-rule {
    position: absolute;
    left: 258px;
    top: 250px;
    width: 584px;
    height: 4px;
    background: var(--brand-red);
  }
  .slogan-top {
    top: 355px;
    font-size: 68px;
    line-height: 80px;
    font-weight: 800;
    color: var(--brand-red);
  }
  .slogan-bottom {
    top: 430px;
    font-size: 66px;
    line-height: 80px;
    font-weight: 700;
    color: var(--sign-white);
  }
  .phone {
    top: 605px;
    font-size: 122px;
    line-height: 136px;
    font-weight: 800;
    color: var(--sign-white);
    letter-spacing: -1px;
  }
  .website-row {
    position: absolute;
    left: 84px;
    right: 84px;
    top: 736px;
    height: 44px;
    display: flex;
    align-items: center;
    gap: 18px;
  }
  .website-row .rule {
    flex: 1;
    height: 2px;
    background: var(--sign-white);
  }
  .website {
    font-size: 36px;
    font-weight: 700;
    color: var(--sign-white);
    white-space: nowrap;
  }
</style>
</head>
<body>
  <div class="yard-sign">
    <svg class="sign-bands" viewBox="0 0 1292 968" preserveAspectRatio="none" aria-hidden="true">
      <rect x="0" y="560" width="1292" height="408" fill="var(--brand-red)"/>
      <path d="M0,400 Q646,232 1292,400 L1292,615 Q646,800 0,628 Z" fill="var(--brand-navy)"/>
      <path d="M0,452 Q420,340 980,352" fill="none" stroke="var(--brand-red)" stroke-width="16"/>
      <path d="M360,376 Q900,326 1292,448" fill="none" stroke="var(--sign-white)" stroke-width="12"/>
      <path d="M0,583 Q480,690 930,645" fill="none" stroke="var(--sign-white)" stroke-width="16"/>
      <path d="M360,670 Q900,705 1292,582" fill="none" stroke="var(--brand-red)" stroke-width="12"/>
    </svg>

    <p class="line brand-name">PL Dunmore</p>
    <p class="line brand-trade">Electrical Contractor</p>
    <div class="brand-rule"></div>

    <p class="line slogan-top">Built on Integrity</p>
    <p class="line slogan-bottom">Driven by Excellence</p>

    <p class="line phone">555-214-7796</p>
    <div class="website-row">
      <span class="rule"></span>
      <span class="website">pldunmoreelectric.example</span>
      <span class="rule"></span>
    </div>
  </div>
</body>
</html>
```